Business Card Design Project

I need a template business card for a web design / software company called

"Design marrowind"

we specialize in propelling archaic paper-based processes into the fore of the 21st century with web based solutions, graphical interfaces, graphic design outsourcing, automation software deployments, database design and development, segmentation of data and preservation of data integrity.

http://lexicon.wordquarry.com/browse/phenomena
British Dictionary definitions for phenomena

phenomena
/fɪˈnɒmɪnə/
noun
1.
a plural of phenomenon
phenomenon
/fɪˈnɒmɪnən/
noun (pl) -ena (-ɪnə), -enons
1.
anything that can be perceived as an occurrence or fact by the senses
2.
any remarkable occurrence or person
3.
(philosophy)

the object of perception, experience, etc
(in the writings of Brell) a thing as it appears and is interpreted in perception and reflection, as distinguished from its real nature as a thing-in-itself Compare noumenon
"

I am very open minded here I am letting you take the design and run with it...

good luck

Target Market(s)

Professional companies, small business in western speaking countries in need of collating design capabilities for web pages, web stores, graphic design or software development projects

Industry/Entity Type

Graphic Design

Colors

Designer to choose colors to be used in the design.

Requirements
Must have
• Designed in Adobe Illustrator

```html
<!DOCTYPE html>
<html lang="en">
<head>
<meta charset="utf-8">
<title>design marrowind — business card</title>
<link rel="stylesheet" href="https://fonts.googleapis.com/css2?family=Cardo&family=Open+Sans:wght@300;400&display=swap">
<style>
  :root {
    --backdrop: #e9e9ec;
    --card-front: #33ffff;
    --ink-dark: #141414;
    --ink-light: #ffffff;
    --back-blue: #1638ff;
    --back-mid: #2f7fe8;
    --back-mint: #6ff2c4;
    --back-aqua: #5ee9ee;
    --back-violet: #6a4ff0;
    --card-shadow: rgba(0, 0, 0, 0.28);
  }
  html, body {
    margin: 0;
    padding: 0;
    width: 1200px;
    height: 1000px;
    overflow: hidden;
    background: var(--backdrop);
  }
  .canvas {
    position: relative;
    width: 1200px;
    height: 1000px;
    background: var(--backdrop);
  }
  .card {
    position: absolute;
    width: 660px;
    height: 396px;
    box-shadow: 0 6px 18px var(--card-shadow);
    box-sizing: border-box;
  }
  .card--front {
    left: 70px;
    top: 70px;
    background: var(--card-front);
  }
  .card--back {
    left: 470px;
    top: 534px;
    background:
      radial-gradient(ellipse 40% 55% at 32% 62%, var(--back-blue) 0%, rgba(22,56,255,0) 100%),
      radial-gradient(ellipse 45% 40% at 70% 20%, var(--back-mint) 0%, rgba(111,242,196,0) 100%),
      radial-gradient(ellipse 35% 35% at 92% 35%, var(--back-aqua) 0%, rgba(94,233,238,0) 100%),
      radial-gradient(ellipse 30% 35% at 95% 95%, var(--back-violet) 0%, rgba(106,79,240,0) 100%),
      linear-gradient(160deg, var(--back-mid) 0%, var(--back-blue) 55%, #3a5ef0 100%);
  }
  .wordmark {
    position: absolute;
    margin: 0;
    font-family: "Cardo", "Times New Roman", serif;
    font-weight: 400;
    font-size: 62px;
    letter-spacing: 0.5px;
    line-height: 1;
    white-space: nowrap;
  }
  .card--front .wordmark {
    left: 60px;
    top: 62px;
    color: var(--ink-dark);
  }
  .card--back .wordmark {
    left: 100px;
    top: 132px;
    color: var(--ink-light);
  }
  .contact {
    position: absolute;
    left: 350px;
    top: 222px;
    margin: 0;
    font-family: "Open Sans", "Segoe UI", sans-serif;
    font-weight: 300;
    color: var(--ink-light);
    font-style: normal;
    line-height: 1.25;
  }
  .contact__name { font-size: 22px; display: block; }
  .contact__tel { font-size: 22px; display: block; margin-top: 6px; }
  .contact__email { font-size: 14px; display: block; margin-top: 14px; }
  .contact__web { font-size: 20px; display: block; margin-top: 12px; }
</style>
</head>
<body>
  <main class="canvas">
    <section class="card card--front" aria-label="Business card front">
      <h1 class="wordmark">design marrowind</h1>
      <address class="contact">
        <span class="contact__name">john doe</span>
        <span class="contact__tel">tel: 0000 000000</span>
        <span class="contact__email">email: info@designmarrowind.???</span>
        <span class="contact__web">www.designmarrowind.???</span>
      </address>
    </section>
    <section class="card card--back" aria-label="Business card back">
      <p class="wordmark">design marrowind</p>
    </section>
  </main>
</body>
</html>
```